Bright Sprouts Business Card

speech therapy business card that is fun and professional using my logo.

Wow wonderful dedigns ... 

Industry/Entity Type

Business

Contact Information for Business Card

Rosa Vantrell
Corvid Certified Practising Speech Pathologist
B.Sp.Path MRTQB CRTP
ph: 0419364720
brightsprotsspeechpathology@mailtrove.example
www.brightsproutsspeechpathology.example

```html
<!DOCTYPE html>
<html lang="en">
<head>
<meta charset="utf-8">
<title>Bright Sprouts Speech Pathology – Business Card</title>
<link rel="stylesheet" href="https://fonts.googleapis.com/css2?family=Cabin:wght@400;500&family=Open+Sans:wght@400&display=swap">
<style>
  :root {
    --backdrop: #2b2b2b;
    --card: #ffffff;
    --card-tint: #eef5fb;
    --brand-blue: #1e7fb8;
    --brand-plum: #9c2a5a;
    --ink: #2a2a2a;
    --rule: #d4dbe2;
  }
  * { box-sizing: border-box; margin: 0; padding: 0; }
  html, body {
    width: 1200px; height: 900px; overflow: hidden;
    background: var(--backdrop);
  }
  .stage { position: relative; width: 1200px; height: 900px; }

  .card {
    position: absolute;
    width: 520px; height: 300px;
    background: linear-gradient(135deg, var(--card) 0%, var(--card) 55%, var(--card-tint) 100%);
    box-shadow: 0 12px 30px rgba(0,0,0,.5);
    overflow: hidden;
  }
  .card__band {
    position: absolute; left: 0; right: 0; bottom: 0;
    height: 28px; background: var(--brand-blue);
  }
  .card--front { left: 60px; top: 440px; }
  .card--back { left: 620px; top: 170px; }

  .wordmark {
    display: flex; align-items: center; gap: 14px;
    font-family: "Cabin", sans-serif; font-weight: 500;
    color: var(--brand-blue); line-height: 1.05;
  }
  .wordmark__dot {
    flex: none; border-radius: 50%; background: var(--brand-blue);
  }
  .card--front .wordmark {
    position: absolute; left: 70px; top: 82px; font-size: 44px;
  }
  .card--front .wordmark__dot { width: 56px; height: 56px; }

  .card--back .wordmark {
    position: absolute; left: 16px; top: 92px; width: 184px;
    flex-direction: column; align-items: center; text-align: center;
    gap: 10px; font-size: 22px;
  }
  .card--back .wordmark__dot { width: 38px; height: 38px; }

  .card__divider {
    position: absolute; left: 212px; top: 34px; bottom: 60px;
    width: 1px; background: var(--rule);
  }
  .contact { position: absolute; left: 230px; top: 46px; right: 14px; }
  .contact__name {
    font-family: "Cabin", sans-serif; font-weight: 400;
    font-size: 24px; color: var(--brand-blue);
  }
  .contact__title {
    margin-top: 8px;
    font-family: "Cabin", sans-serif; font-size: 13px;
    color: var(--brand-plum); line-height: 1.3;
  }
  .contact__list { list-style: none; margin-top: 22px; }
  .contact__item {
    display: flex; align-items: center; gap: 8px;
    font-family: "Open Sans", sans-serif; font-size: 10px;
    color: var(--ink); margin-bottom: 10px;
    white-space: nowrap;
  }
  .contact__icon { flex: none; width: 13px; height: 13px; }
</style>
</head>
<body>
<main class="stage">

  <section class="card card--front" aria-label="Card front">
    <div class="wordmark">
      <span class="wordmark__dot"></span>
      <span>Bright Sprouts<br>Speech Pathology</span>
    </div>
    <div class="card__band"></div>
  </section>

  <section class="card card--back" aria-label="Card back">
    <div class="wordmark">
      <span class="wordmark__dot"></span>
      <span>Bright Sprouts<br>Speech Pathology</span>
    </div>
    <div class="card__divider"></div>
    <div class="contact">
      <h1 class="contact__name">Rosa Vantrell Corvid</h1>
      <p class="contact__title">Certified Practising Speech Pathologist<br>B.Sp.Path MRTQB CRTP</p>
      <ul class="contact__list">
        <li class="contact__item">
          <svg class="contact__icon" viewBox="0 0 16 16"><path fill="#1e7fb8" d="M4 1l3 3-1.6 1.8c.8 1.8 2.2 3.2 4 4L11.2 8.2l3 3L12.5 14C7 13.5 2.5 9 2 3.5z"/></svg>
          <span>0419364720</span>
        </li>
        <li class="contact__item">
          <svg class="contact__icon" viewBox="0 0 16 16"><rect x="1" y="3" width="14" height="10" rx="1" fill="#1e7fb8"/><path d="M1.5 4l6.5 5 6.5-5" fill="none" stroke="#fff" stroke-width="1.3"/></svg>
          <span>brightsprotsspeechpathology@mailtrove.example</span>
        </li>
        <li class="contact__item">
          <svg class="contact__icon" viewBox="0 0 16 16" fill="none" stroke="#1e7fb8" stroke-width="1.3"><circle cx="8" cy="8" r="6.5"/><ellipse cx="8" cy="8" rx="3" ry="6.5"/><path d="M1.5 8h13"/></svg>
          <span>www.brightsproutsspeechpathology.example</span>
        </li>
      </ul>
    </div>
    <div class="card__band"></div>
  </section>

</main>
</body>
</html>
```